VORL Feature Icons

We have existing feature icons we would like to redesign.
See existing icons at http://www.vorltechnik.example/vorl-platform. Single color icons are prefered, flat design.

I would also like a new "wrapper" icon for our agents and plugins. We currently use a "circle" icon with different graphics inside representing different tech. I would like another take on the "circle" and still be able to use tech graphic inside. See existing wrapper icon at http://www.vorltechnik.example/vorl-plugins

Target Market(s)

Enterprise, B2B

Requirements
Must have
• Colors should fit existing palette on the website

```html
<!DOCTYPE html>
<html lang="en">
<head>
<meta charset="utf-8">
<title>VORL Feature Icons</title>
<link href="https://fonts.googleapis.com/css2?family=Lato:wght@400&display=swap" rel="stylesheet">
<style>
  :root {
    --brand: #1a5e8a;
    --ink: #474747;
    --paper: #ffffff;
  }
  * { box-sizing: border-box; margin: 0; padding: 0; }
  html, body { width: 1200px; height: 1200px; overflow: hidden; background: var(--paper); }
  .canvas { position: relative; width: 1200px; height: 1200px; font-family: 'Lato', sans-serif; }
  .feature-grid {
    position: absolute; left: 65px; top: 44px;
    display: grid; grid-template-columns: repeat(3, 357px); grid-auto-rows: 250px;
  }
  .feature { display: flex; flex-direction: column; align-items: center; text-align: center; }
  .feature-icon { width: 120px; height: 120px; fill: var(--brand); }
  .feature-icon .stroke { fill: none; stroke: var(--brand); }
  .icon-placeholder { width: 110px; height: 120px; background: var(--brand); border-radius: 50% 50% 12px 12px; }
  .feature-text { margin-top: 44px; width: 330px; color: var(--ink); font-size: 15.5px; line-height: 27px; }
  .wrapper-badge {
    position: absolute; top: 1030px; width: 152px; height: 152px; border-radius: 50%;
    border: 3px solid var(--brand); display: flex; align-items: center; justify-content: center;
  }
  .wrapper-badge::before {
    content: ""; position: absolute; inset: 7px; border-radius: 50%; border: 2px solid var(--brand);
  }
  .badge-apis { left: 367px; }
  .badge-partner { left: 672px; }
  .badge-label { color: var(--ink); font-size: 21px; }
  .badge-partner .badge-label { color: var(--brand); font-size: 17px; }
</style>
</head>
<body>
<div class="canvas">
  <div class="feature-grid">
    <div class="feature">
      <svg class="feature-icon" viewBox="0 0 120 120">
        <g class="stroke" stroke-width="14" stroke-dasharray="6 5"><circle cx="35" cy="52" r="17"/><circle cx="75" cy="25" r="13"/><circle cx="80" cy="84" r="22"/></g>
        <circle cx="35" cy="52" r="14"/><circle cx="75" cy="25" r="10"/><circle cx="80" cy="84" r="19"/>
        <g fill="#fff"><circle cx="35" cy="52" r="6"/><circle cx="75" cy="25" r="4"/><circle cx="80" cy="84" r="8"/></g>
      </svg>
      <p class="feature-text">VORL focuses on your integrations. On-premises, cloud and custom</p>
    </div>
    <div class="feature">
      <div class="icon-placeholder" role="img" aria-label="Silhouette of a head with gears inside"></div>
      <p class="feature-text">Machine learning is used to set dynamic alert thresholds for your integrations</p>
    </div>
    <div class="feature">
      <svg class="feature-icon" viewBox="0 0 120 120">
        <rect x="5" y="5" width="4" height="106"/><rect x="5" y="107" width="112" height="4"/>
        <rect x="18" y="58" width="18" height="50"/><rect x="42" y="36" width="18" height="72"/><rect x="66" y="50" width="18" height="58"/><rect x="90" y="18" width="18" height="90"/>
        <g fill="#fff"><rect x="23" y="63" width="8" height="16"/><rect x="47" y="41" width="8" height="30"/><rect x="71" y="55" width="8" height="24"/><rect x="95" y="23" width="8" height="36"/></g>
      </svg>
      <p class="feature-text">Chart and correlate any metric collected from the VORL agents</p>
    </div>

    <div class="feature">
      <svg class="feature-icon" viewBox="0 0 120 120">
        <path d="M28 98V62a32 32 0 0 1 64 0v36z"/><rect x="18" y="104" width="84" height="10"/>
        <path d="M62 40a18 18 0 0 1 16 18v34h-6V58a12 12 0 0 0-10-12z" fill="#fff"/>
        <g class="stroke" stroke-width="4"><path d="M60 2v14M32 12l7 12M88 12l-7 12M8 34l12 7M112 34l-12 7M2 64h14M104 64h14"/></g>
      </svg>
      <p class="feature-text">VORL can detect anomalies at an early stage and alert you</p>
    </div>
    <div class="feature">
      <svg class="feature-icon" viewBox="0 0 120 120">
        <rect x="2" y="52" width="28" height="18"/><rect x="86" y="52" width="28" height="18"/><rect x="90" y="10" width="28" height="18"/><rect x="78" y="94" width="28" height="18"/>
        <g class="stroke" stroke-width="4"><path d="M36 61h50M50 61V19h40M50 61v42h28M48 51v20"/></g>
      </svg>
      <p class="feature-text">The Topological map provides insight and process overview</p>
    </div>
    <div class="feature">
      <svg class="feature-icon" viewBox="0 0 120 120">
        <rect x="48" y="2" width="10" height="26"/><rect x="78" y="2" width="10" height="26"/>
        <path d="M38 26h60v26a12 12 0 0 1-12 12H50a12 12 0 0 1-12-12z"/>
        <g class="stroke" stroke-width="8"><path d="M68 62v38a14 14 0 0 1-28 0V86a12 12 0 0 0-12-12H2"/></g>
      </svg>
      <p class="feature-text">Use the Plugins to push VORL alerts and information to other systems</p>
    </div>

    <div class="feature">
      <svg class="feature-icon" viewBox="0 0 120 120">
        <path d="M28 86a20 20 0 0 1 0-40 26 26 0 0 1 50-10 22 22 0 0 1 20 26v24z"/>
        <circle cx="88" cy="84" r="30" fill="#fff"/><circle cx="88" cy="84" r="26"/>
        <circle cx="88" cy="84" r="9" fill="#fff"/><circle cx="88" cy="84" r="5"/>
        <g class="stroke" stroke-width="3" stroke="#fff"><path d="M100 62 76 106"/></g>
      </svg>
      <p class="feature-text">VORL can be delivered as a cloud service or complete on-premises install</p>
    </div>
    <div class="feature">
      <div class="icon-placeholder" role="img" aria-label="Group of three people silhouettes" style="width:130px;height:90px;margin:15px 0;border-radius:40px 40px 6px 6px"></div>
      <p class="feature-text">VORL has monitoring agents for integration platforms and peripherals</p>
    </div>
    <div class="feature">
      <svg class="feature-icon" viewBox="0 0 120 120">
        <g class="stroke" stroke-linecap="round"><path d="M14 14l88 88" stroke-width="14"/><path d="M100 20 20 100" stroke-width="12"/></g>
        <circle cx="104" cy="16" r="14"/><circle cx="16" cy="104" r="14"/>
        <g fill="#fff"><circle cx="110" cy="10" r="7"/><circle cx="10" cy="110" r="7"/></g>
      </svg>
      <p class="feature-text">VORL has its own SDK so you can create your own custom agents</p>
    </div>

    <div class="feature">
      <svg class="feature-icon" viewBox="0 0 120 120">
        <rect x="12" y="12" width="96" height="106" rx="5"/><rect x="20" y="22" width="80" height="88" fill="#fff"/>
        <rect x="40" y="4" width="40" height="16" rx="6"/>
        <text x="60" y="64" text-anchor="middle" font-family="Lato, sans-serif" font-size="38">$</text>
        <rect x="34" y="76" width="52" height="4"/><rect x="34" y="84" width="52" height="4"/><rect x="34" y="92" width="52" height="4"/>
      </svg>
      <p class="feature-text">Create reports on any transaction and business metric</p>
    </div>
    <div class="feature">
      <svg class="feature-icon" viewBox="0 0 120 120">
        <rect x="0" y="14" width="96" height="68" rx="3"/><rect x="7" y="21" width="82" height="54" fill="#fff"/>
        <rect x="40" y="82" width="16" height="10"/><rect x="22" y="92" width="52" height="5"/>
        <rect x="80" y="40" width="40" height="62" rx="3" fill="#fff"/><rect x="84" y="44" width="32" height="56" rx="3"/><rect x="88" y="48" width="24" height="44" fill="#fff"/>
      </svg>
      <p class="feature-text">GUI supports access from many devices</p>
    </div>
    <div class="feature">
      <svg class="feature-icon" viewBox="0 0 120 120">
        <g class="stroke" stroke-width="12"><path d="M34 56V36a26 26 0 0 1 52 0v20"/></g>
        <rect x="12" y="52" width="96" height="66" rx="6"/>
        <path d="M60 74a8 8 0 0 1 4 15l2 12h-12l2-12a8 8 0 0 1 4-15z" fill="#fff"/>
      </svg>
      <p class="feature-text">Separate runtime and data storage, encrypted connections</p>
    </div>
  </div>

  <div class="wrapper-badge badge-apis"><span class="badge-label">APIs</span></div>
  <div class="wrapper-badge badge-partner"><span class="badge-label">Nuvatrace</span></div>
</div>
</body>
</html>
```